RAmio Shop Business Card Design

My auto shop is targeted to the European and Asian luxury automotive market. We do mechanics collision and parts.
Some of the makes are KTR, DQ, Stone Herald, Valdine,Norvi, solavanta, bremo, HJ, etc. But in the end we get all makes.
I don't want to have the makes logos on the business card.
The Name of the business is after my first Name Ramiro but without the s Ramio Shop if there is any other ideas about the name iam open to suggestions. And i don't have a LOGO. Need logo!
Updates

Reason: I increased my budget and invited more designers. And committed payment so giving you guys more time.

Target Market(s)

target is the luxury auto market

Industry/Entity Type

Automotive

Contact Information for Business Card

European Automotive Repair Shop, Collision Mechanics Parts
Ramiro Villalba Owner, Colibrí #14 Loma Serena 2

Requirements
Nice to have
• One design i can of liked was the use of the dash error logos like check engine light airbag light. Nobla press has this but dose not include the air bag light. For the collision part of the business. But am open to any design.
Should not have
• exact logo makes on front of card.

```html
<!DOCTYPE html>
<html lang="en">
<head>
<meta charset="utf-8">
<title>Ramio Shop Business Card</title>
<link rel="stylesheet" href="https://fonts.googleapis.com/css2?family=Open+Sans:wght@600;700;800&display=swap">
<style>
  :root {
    --backdrop: #4a423b;
    --card: #000000;
    --brand-red: #e31b23;
    --logo-grey: #5c5c5c;
    --white: #ffffff;
    --silver-dark: #1c1c1c;
    --silver-light: #e8e8e8;
  }
  html, body {
    margin: 0;
    width: 1200px;
    height: 1000px;
    overflow: hidden;
    background: var(--backdrop);
    font-family: "Open Sans", Arial, sans-serif;
  }
  .card {
    position: absolute;
    left: 240px;
    width: 720px;
    height: 410px;
    background: var(--card);
    border-radius: 34px;
    overflow: hidden;
    box-shadow: 0 10px 30px rgba(0,0,0,.45);
  }
  .card--front { top: 60px; }
  .card--back { top: 530px; }

  .silver-band {
    position: absolute;
    left: 0;
    right: 0;
    height: 9px;
    background: linear-gradient(90deg, var(--silver-dark) 0%, #555 30%, var(--silver-light) 55%, #555 78%, var(--silver-dark) 100%);
  }

  /* Front */
  .brand-lockup {
    position: absolute;
    left: 0; right: 0;
    top: 140px;
    display: flex;
    justify-content: center;
    align-items: center;
    gap: 22px;
  }
  .brand-lockup__mark {
    width: 38px; height: 38px;
    border-radius: 50%;
    background: var(--brand-red);
  }
  .brand-lockup__name {
    font-weight: 800;
    font-size: 84px;
    letter-spacing: 2px;
    color: var(--logo-grey);
    line-height: 1;
  }
  .card--front .silver-band { top: 340px; }

  /* Back */
  .back-content {
    position: absolute;
    left: 0; right: 0; top: 26px;
    text-align: center;
  }
  .back-title {
    margin: 0;
    font-weight: 800;
    font-size: 42px;
    letter-spacing: 1.5px;
    color: var(--brand-red);
    line-height: 1.1;
  }
  .back-tagline {
    margin: 2px 0 0;
    font-weight: 700;
    font-size: 30px;
    color: var(--white);
    letter-spacing: .5px;
  }
  .service-icons {
    display: flex;
    justify-content: space-between;
    width: 470px;
    margin: 14px auto 0;
    align-items: center;
  }
  .service-icons svg { display: block; }
  .services {
    margin: 6px 0 0;
    font-weight: 700;
    font-size: 21px;
    color: var(--white);
  }
  .owner {
    margin: 10px 0 0;
    font-weight: 800;
    font-size: 29px;
    color: var(--brand-red);
    line-height: 1.1;
  }
  .address {
    margin: 0;
    font-weight: 700;
    font-size: 20px;
    color: var(--white);
    line-height: 1.25;
  }
  .card--back .silver-band--upper { top: 318px; }
  .card--back .silver-band--lower { top: 392px; }
  .contact {
    position: absolute;
    display: flex;
    align-items: center;
    gap: 8px;
    font-weight: 700;
    font-size: 17px;
    letter-spacing: 1px;
    color: var(--white);
  }
  .contact--phone { left: 40px; top: 340px; }
  .contact--fax { right: 40px; top: 362px; }
</style>
</head>
<body>

<section class="card card--front" aria-label="Card front">
  <div class="brand-lockup">
    <span class="brand-lockup__mark"></span>
    <span class="brand-lockup__name">RAMIO SHOP</span>
  </div>
  <div class="silver-band"></div>
</section>

<section class="card card--back" aria-label="Card back">
  <div class="back-content">
    <h1 class="back-title">RAMIO SHOP</h1>
    <p class="back-tagline">European Automotive Repair Shop</p>

    <div class="service-icons">
      <svg class="icon-engine" width="70" height="44" viewBox="0 0 70 44" aria-label="Check engine light" role="img">
        <g fill="none" stroke="#e31b23" stroke-width="4" stroke-linejoin="round">
          <path d="M14 12 H48 L54 18 H62 V34 H54 L48 40 H20 L14 34 H8 V18 H14 Z"/>
          <path d="M26 4 H40 M33 4 V12"/>
          <path d="M2 20 V32"/>
        </g>
      </svg>
      <svg class="icon-battery" width="56" height="44" viewBox="0 0 56 44" aria-label="Battery warning light" role="img">
        <rect x="8" y="0" width="10" height="6" fill="#e31b23"/>
        <rect x="38" y="0" width="10" height="6" fill="#e31b23"/>
        <rect x="2" y="6" width="52" height="36" rx="3" fill="#e31b23"/>
        <path d="M30 12 L22 26 H29 L25 37 L35 22 H28 L32 12 Z" fill="#000"/>
      </svg>
      <div role="img" aria-label="Airbag warning light" style="width:40px;height:40px;border-radius:8px;background:#e31b23;"></div>
    </div>

    <p class="services">Collision Mechanics Parts</p>
    <p class="owner">Ramiro Villalba</p>
    <p class="address">Colibrí<br>#14 Loma Serena 2</p>
  </div>

  <div class="silver-band silver-band--upper"></div>

  <div class="contact contact--phone">
    <svg width="12" height="18" viewBox="0 0 12 18" aria-hidden="true">
      <rect x="1" y="1" width="10" height="16" rx="2" fill="none" stroke="#e31b23" stroke-width="2"/>
      <rect x="4" y="13" width="4" height="2" fill="#e31b23"/>
    </svg>
    <span>55501234567</span>
  </div>

  <div class="contact contact--fax">
    <span>55501234567</span>
    <svg width="18" height="18" viewBox="0 0 18 18" aria-hidden="true">
      <rect x="4" y="1" width="10" height="6" fill="none" stroke="#e31b23" stroke-width="2"/>
      <rect x="1" y="7" width="16" height="10" rx="2" fill="none" stroke="#e31b23" stroke-width="2"/>
      <rect x="5" y="11" width="8" height="2" fill="#e31b23"/>
    </svg>
  </div>

  <div class="silver-band silver-band--lower"></div>
</section>

</body>
</html>
```